Harbor Crest PEO - Web Build for Professional Employment Organization

We need a website built for our new PEO (professional employment organization). This company will offer third party Human Resource services to companies who are looking to outsource:<br/>Recruiting<br/>Administrative Onboarding<br/>New hire training, ongoing training and development<br/>Payroll/compensation processing/services<br/>Employee Relations<br/>Unemployment Claim Facilitation<br/>Benefits Plans and Administration<br/><br/>I have attached the logo below. Please use that as a reference and color match as best as possible. <br/><br/>Here are some of the competitor's websites:<br/>https://www.velmorix.example/ <br/>https://www.quandrel.example/<br/>https://www.quandrel.example/<br/>https://www.tzv.example/<br/>https://www.brindaxo.example/<br/>https://lumbrasto.example/contact-lumbra/<br/><br/>

Target Market(s)

Startups and mid-sized businesses

Number of Pages Required

5+ page

Font styles to use
Sans Serif

Colors
0592cd

Requirements
Must have
• Features Pages
• SEO driven keyword rich content
• Strong focus on our ability to provide unemployment claim facilitation services as well as mandatory training/certification fulfillment
Nice to have
• I'd like to see one mockup with a Live Chat version if possible. In theory, the Live Chat messages would go directly to our front desk person.

```html
<!DOCTYPE html>
<html lang="en">
<head>
<meta charset="utf-8">
<title>Harbor Crest PEO</title>
<link href="https://fonts.googleapis.com/css2?family=Poppins:wght@400;500;600;700&display=swap" rel="stylesheet">
<style>
:root{
  --slate:#475570;
  --slate-dark:#3e4a62;
  --slate-band:#4b5a76;
  --ink:#2b2f38;
  --teal:#1b9ab3;
  --teal-light:#35b9cf;
  --accent:#0592cd;
  --line:#e4e7ec;
  --muted:#5b6170;
  --foot-link:#b6bfd0;
  --award-bg:#f1f1f1;
}
*{margin:0;padding:0;box-sizing:border-box}
html,body{width:1200px;height:2206px;overflow:hidden}
body{font-family:'Poppins',sans-serif;color:var(--ink);background:#fff;position:relative}
.abs{position:absolute}
a{color:inherit;text-decoration:none}

.top-bar{left:0;top:0;width:1200px;height:30px;background:var(--slate)}
.top-bar nav{position:absolute;right:234px;top:9px;display:flex;gap:17px;font-size:7.5px;font-weight:500;color:#fff;letter-spacing:.2px}

.site-header{left:0;top:30px;width:1200px;height:86px;background:#fff}
.brand{position:absolute;font-weight:600;color:var(--teal);letter-spacing:.5px;white-space:nowrap}
.brand-header{left:234px;top:26px;font-size:20px}
.brand small{display:block;font-size:9px;letter-spacing:6px;text-align:center;color:var(--slate);border-top:1.5px solid var(--teal);margin-top:2px;padding-top:1px}
.main-nav{position:absolute;left:485px;top:40px;display:flex;gap:26px;font-size:8.5px;font-weight:500;color:var(--ink)}
.btn{display:flex;align-items:center;justify-content:center;gap:7px;background:linear-gradient(90deg,var(--teal),var(--teal-light));color:#fff;font-weight:600;border-radius:2px}
.btn-start{position:absolute;left:854px;top:27px;width:112px;height:32px;font-size:9px}

.hero{left:0;top:116px;width:1200px;height:375px;background:linear-gradient(110deg,#7b7f82 0%,#9a9a8e 45%,#b4a98e 60%,#9d9790 80%,#cfd3d6 100%)}
.hero-shade{left:0;top:116px;width:1200px;height:375px}
.hero-copy{left:0;top:116px;width:1200px;height:375px}
.hero-title{position:absolute;left:234px;top:139px;font-size:22px;line-height:25px;font-weight:700;color:#fff;letter-spacing:.2px}
.btn-hero{position:absolute;left:234px;top:209px;width:143px;height:33px;font-size:8.5px}

.section-title{position:absolute;left:0;width:1200px;text-align:center;font-size:18.5px;font-weight:500;color:var(--ink)}

.services{left:234px;top:600px;width:732px;height:260px;display:grid;grid-template-columns:178px 188px 187px 179px;grid-template-rows:130px 130px}
.service{display:flex;flex-direction:column;align-items:center;text-align:center;padding-top:18px;border-right:1px solid var(--line)}
.service:nth-child(4n){border-right:none}
.service:nth-child(-n+4){border-bottom:1px solid var(--line)}
.service svg{width:42px;height:42px;stroke:var(--slate);fill:none;stroke-width:1.3}
.service svg .hl{stroke:var(--teal)}
.service h3{font-size:11px;font-weight:500;line-height:16px;margin-top:7px;color:var(--ink)}
.learn{font-size:7.5px;color:var(--teal);margin-top:4px;display:flex;align-items:center;gap:3px}
.learn i{display:inline-block;width:7px;height:7px;border:1px solid var(--teal);border-radius:50%}

.testimonial{left:0;top:917px;width:600px;height:300px;background:var(--slate-band)}
.testimonial h2{position:absolute;left:234px;top:55px;font-size:15px;font-weight:700;color:#fff}
.testimonial p{position:absolute;left:234px;top:92px;width:330px;font-size:8.6px;line-height:16.4px;color:#fff}
.btn-stories{position:absolute;left:234px;top:198px;width:143px;height:32px;font-size:8.5px}
.video{left:600px;top:917px;width:600px;height:300px;background:linear-gradient(120deg,#2a9bb4 0%,#3fb3c8 55%,#2aa2b9 100%)}
.play{left:869px;top:1036px;width:62px;height:62px}

.news-card{top:1324px;width:232px;height:340px;border:1px solid var(--line);background:#fff}
.news-photo{position:absolute;left:0;top:0;width:230px;height:151px}
.news-dot{position:absolute;left:99px;top:134px;width:34px;height:34px;border-radius:50%;background:#fff;box-shadow:0 1px 4px rgba(0,0,0,.12)}
.news-card h3{position:absolute;left:15px;top:175px;width:200px;font-size:13.2px;line-height:19px;font-weight:500}
.news-date{position:absolute;left:16px;top:222px;font-size:8.5px;color:var(--muted);display:flex;align-items:center;gap:5px}
.news-date i{display:inline-block;width:8px;height:8px;border:1px solid var(--teal);border-top-width:2px}
.news-card p{position:absolute;left:17px;top:242px;width:195px;font-size:8.6px;line-height:15px;color:var(--muted)}
.news-more{position:absolute;left:18px;top:312px;font-size:8.8px;color:var(--teal);text-decoration:underline}

.awards{left:0;top:1720px;width:1200px;height:126px;background:var(--award-bg)}
.badge{position:absolute}

.site-footer{left:0;top:1846px;width:1200px;height:302px;background:var(--slate)}
.foot-top{position:absolute;left:0;top:0;width:1200px;height:84px;border-bottom:1px solid #56637d}
.divider{position:absolute;top:0;width:1px;height:84px;background:#56637d}
.brand-footer{left:234px;top:30px;font-size:19px;color:#fff}
.brand-footer small{color:#fff}
.follow{position:absolute;left:739px;top:38px;font-size:8.5px;color:#fff}
.social{position:absolute;top:31px;width:27px;height:27px;background:#56637d;border-radius:2px}
.foot-col{position:absolute;top:124px}
.foot-col h4{font-size:8.3px;font-weight:600;color:#fff;margin-bottom:7px}
.foot-col li{list-style:none;font-size:7px;color:var(--foot-link);line-height:16.3px}
.foot-col h4.gap{margin-top:12px}

.bottom-bar{left:0;top:2148px;width:1200px;height:58px;background:var(--slate-dark);font-size:7.5px;color:var(--foot-link)}
.bottom-bar .copy{position:absolute;left:235px;top:27px}
.bottom-bar .legal{position:absolute;right:235px;top:27px;display:flex;gap:10px}
</style>
</head>
<body>

<header class="abs top-bar">
  <nav><a>LOGIN</a><a>INTEGRATIONS</a><a>PARTNERS</a><a>INVESTORS</a></nav>
</header>

<div class="abs site-header">
  <div class="brand brand-header">HARBOR CREST<small>P E O</small></div>
  <nav class="main-nav"><a>WHAT WE DO</a><a>WHO WE ARE</a><a>INSIGHTS</a><a>CAREERS</a><a>CONTACT</a></nav>
  <a class="btn btn-start">Let's Get Started</a>
</div>

<section>
  <div class="abs hero" role="img" aria-label="Photo of a team meeting in a bright office, a presenter at a whiteboard"></div>
  <svg class="abs hero-shade" viewBox="0 0 1200 375" aria-hidden="true">
    <defs><linearGradient id="shade" x1="0" x2="1"><stop offset="0" stop-color="#3d4a64" stop-opacity=".75"/><stop offset="1" stop-color="#3d4a64" stop-opacity=".45"/></linearGradient></defs>
    <polygon points="0,0 672,0 591,375 0,375" fill="url(#shade)"/>
  </svg>
  <div class="abs hero-copy">
    <h1 class="hero-title">Powerful HR solutions with<br>exceptional follow-through</h1>
    <a class="btn btn-hero">Explore HR Solutions <span>&#9656;</span></a>
  </div>
</section>

<h2 class="section-title" style="top:538px">All-in-one Payroll &amp; HR</h2>

<section class="abs services">
  <div class="service">
    <svg viewBox="0 0 42 42"><rect x="10" y="5" width="22" height="33" rx="2"/><rect x="16" y="2" width="10" height="6" class="hl"/><circle cx="21" cy="17" r="4" class="hl"/><path d="M14 28c2-5 12-5 14 0M14 33h14"/></svg>
    <h3>Recruiting</h3><span class="learn">LEARN MORE <i></i></span>
  </div>
  <div class="service">
    <svg viewBox="0 0 42 42"><circle cx="15" cy="15" r="7" class="hl"/><circle cx="15" cy="15" r="11"/><rect x="22" y="21" width="15" height="17"/><path d="M25 26h9M25 31h9M25 35h6" class="hl"/></svg>
    <h3>Administrative<br>Onboarding</h3><span class="learn">LEARN MORE <i></i></span>
  </div>
  <div class="service">
    <svg viewBox="0 0 42 42"><rect x="16" y="6" width="22" height="17"/><circle cx="9" cy="9" r="3.5" class="hl"/><path d="M6 38V16h7v22M13 18l9 3M27 23l-5 12M27 23l5 12" /><path d="M20 12h14M20 17h10" class="hl"/></svg>
    <h3>New Hire Training</h3><span class="learn">LEARN MORE <i></i></span>
  </div>
  <div class="service">
    <svg viewBox="0 0 42 42"><path d="M12 38v-7c-6-4-7-14-1-20 6-6 18-5 21 3 2 5 0 6 3 10l-3 1v5h-5v8"/><circle cx="17" cy="14" r="4" class="hl"/><circle cx="25" cy="19" r="3" class="hl"/></svg>
    <h3>Ongoing Training and<br>Development</h3><span class="learn">LEARN MORE <i></i></span>
  </div>
  <div class="service">
    <svg viewBox="0 0 42 42"><circle cx="18" cy="12" r="7"/><path d="M4 36c1-9 8-13 14-13s10 3 12 6"/><circle cx="31" cy="31" r="7" class="hl"/><path d="M31 27v8M29 29h4M29 33h4" class="hl"/></svg>
    <h3>Payroll/Compensation<br>Processing/Services</h3><span class="learn">LEARN MORE <i></i></span>
  </div>
  <div class="service">
    <svg viewBox="0 0 42 42"><path d="M20 14h-8a7 7 0 0 0 0 14h8v-5h-8a2 2 0 0 1 0-4h8z"/><path d="M18 14v5M18 23v5" class="hl"/><circle cx="32" cy="7" r="3" class="hl"/><path d="M29 13h6v14h-2v10h-2V27h-2z"/></svg>
    <h3>Employee Relations</h3><span class="learn">LEARN MORE <i></i></span>
  </div>
  <div class="service">
    <svg viewBox="0 0 42 42"><path d="M8 4h18l6 6v26H8z"/><path d="M12 12h10M12 17h14M12 22h8" class="hl"/><circle cx="30" cy="27" r="4" class="hl"/><path d="M22 39c1-5 4-7 8-7s7 2 8 7"/></svg>
    <h3>Unemployment<br>Claim Facilitation</h3><span class="learn">LEARN MORE <i></i></span>
  </div>
  <div class="service">
    <svg viewBox="0 0 42 42"><circle cx="18" cy="12" r="7"/><path d="M4 36c1-9 8-13 14-13s8 2 10 4"/><circle cx="31" cy="30" r="6" class="hl"/><circle cx="31" cy="30" r="2" class="hl"/></svg>
    <h3>Benefits Plans and<br>Administration</h3><span class="learn">LEARN MORE <i></i></span>
  </div>
</section>

<section>
  <div class="abs testimonial">
    <h2>What Are Our Clients Saying?</h2>
    <p>Lorem ipsum dolor sit amet, consectetur adipiscing elit. Nunc in finibus quam. Integer at ullamcorper augue. Orci varius natoque penatibus et magnis dis parturient montes, nascetur ridiculus mus. Vivamus tellus justo, lacinia quis arcu nec, tempor posuere mauris. Curabitur mollis elit in purus tempor commodo.</p>
    <a class="btn btn-stories">Client Success Stories <span>&#9656;</span></a>
  </div>
  <div class="abs video" role="img" aria-label="Video still of a smiling client wearing glasses, tinted teal"></div>
  <svg class="abs play" viewBox="0 0 62 62" aria-hidden="true"><circle cx="31" cy="31" r="29" fill="rgba(255,255,255,.15)" stroke="#fff" stroke-width="3"/><path d="M26 23l12 8-12 8z" fill="#fff"/></svg>
</section>

<h2 class="section-title" style="top:1266px">Latest News</h2>

<article class="abs news-card" style="left:234px">
  <div class="news-photo" role="img" aria-label="Photo of a business team standing in a meeting room" style="background:linear-gradient(135deg,#d9dde2,#8c929b 60%,#e6e8ea)"></div>
  <div class="news-dot"></div>
  <h3>Cras posuere vestibulum quam ut varius.</h3>
  <div class="news-date"><i></i>28/01/2020</div>
  <p>Proin tortor erat, viverra ultrices dapibus eget, placerat non libero. Proin quis interdum neque, sit amet ornare nisi. Suspendisse ac viverra metus.</p>
  <a class="news-more">Find out more</a>
</article>
<article class="abs news-card" style="left:484px">
  <div class="news-photo" role="img" aria-label="Photo of two colleagues reviewing a glowing building model" style="background:linear-gradient(135deg,#9fb3bf,#4fc3c9 45%,#8aa0ad)"></div>
  <div class="news-dot"></div>
  <h3>Cras posuere vestibulum quam ut varius.</h3>
  <div class="news-date"><i></i>28/01/2020</div>
  <p>Proin tortor erat, viverra ultrices dapibus eget, placerat non libero. Proin quis interdum neque, sit amet ornare nisi. Suspendisse ac viverra metus.</p>
  <a class="news-more">Find out more</a>
</article>
<article class="abs news-card" style="left:734px">
  <div class="news-photo" role="img" aria-label="Photo of a job interview across a wooden table" style="background:linear-gradient(135deg,#e4e6e8,#6e6a68 55%,#c9b08a)"></div>
  <div class="news-dot"></div>
  <h3>Cras posuere vestibulum quam ut varius.</h3>
  <div class="news-date"><i></i>28/01/2020</div>
  <p>Proin tortor erat, viverra ultrices dapibus eget, placerat non libero. Proin quis interdum neque, sit amet ornare nisi. Suspendisse ac viverra metus.</p>
  <a class="news-more">Find out more</a>
</article>

<section class="abs awards" aria-label="Awards">
  <div class="badge" style="left:298px;top:24px;width:52px;height:82px;background:#d5d8d6"></div>
  <div class="badge" style="left:398px;top:22px;width:68px;height:86px;background:#d9d9d9;border-radius:4px"></div>
  <div class="badge" style="left:516px;top:24px;width:50px;height:78px;background:#c6c6c6"></div>
  <div class="badge" style="left:617px;top:28px;width:68px;height:72px;background:#d8c8c8;border-radius:50%"></div>
  <div class="badge" style="left:734px;top:22px;width:46px;height:84px;background:#cdc4d8"></div>
  <div class="badge" style="left:840px;top:22px;width:48px;height:84px;background:#2b2b2b"></div>
</section>

<footer class="abs site-footer">
  <div class="foot-top">
    <div class="brand brand-footer">HARBOR CREST<small>P E O</small></div>
    <span class="divider" style="left:433px"></span>
    <span class="divider" style="left:716px"></span>
    <span class="follow">Follow Us</span>
    <span class="social" style="left:806px"></span>
    <span class="social" style="left:838px"></span>
    <span class="social" style="left:870px"></span>
    <span class="social" style="left:903px"></span>
  </div>
  <div class="foot-col" style="left:234px"><h4>PRODUCT TOUR</h4><ul><li>PAYROLL</li><li>HUMAN RESOURCES</li><li>BENEFIT ADMIN TECH</li><li>TIME &amp; LABOR</li><li>TALENT MANAGEMENT</li><li>ENGAGEMENT</li><li>MOBILE</li></ul></div>
  <div class="foot-col" style="left:359px"><h4>INTEGRATIONS</h4><ul><li>MARKETPLACE</li><li>API LIBRARY</li><li>WEBHOOKS</li></ul><h4 class="gap">PARTNERS</h4><h4>INVESTORS</h4></div>
  <div class="foot-col" style="left:485px"><h4>WHY BRINDAXO</h4><ul><li>AWARDS</li><li>TESTIMONIALS</li><li>SECURITY</li><li>LEADERSHIP</li><li>COMMITMENTS</li><li>AMBASSADORS</li></ul><h4 class="gap">CAREERS</h4></div>
  <div class="foot-col" style="left:611px"><h4>RESOURCES</h4><ul><li>CONTENT LIBRARY</li><li>CLIENT TRAINING</li><li>BLOG</li><li>NEWS</li></ul><h4 class="gap">LOGIN</h4></div>
  <div class="foot-col" style="left:734px"><h4>QUICK LINKS</h4><ul><li>ABOUT US</li><li>RESOURCES</li><li>CAREERS</li><li>CONTACT US</li></ul></div>
</footer>

<div class="abs bottom-bar">
  <span class="copy">copyright © 2020 HARBOR CREST PEO. All Rights Reserved.</span>
  <span class="legal"><a>Privacy Policy</a><span>|</span><a>Site Map</a></span>
</div>

</body>
</html>
```